Business Card Ayurvedic Massage

I'm starting with my ayurvedic massage business and need a business card design. The design should be inline with my brand/logo as well as with the design of my website (www.mirelo-dant.ch).
Front: logo and text "Ayurvedische Massagen"
back: name and adress (see details https://www.mirelo-dant.ch/kontakt.html)

```html
<!DOCTYPE html>
<html lang="de">
<head>
<meta charset="utf-8">
<title>Mirelo-Dant – Visitenkarte</title>
<link rel="stylesheet" href="https://fonts.googleapis.com/css2?family=Kurale&family=Tinos:wght@400;700&display=swap">
<style>
  :root {
    --maroon: #7a0c12;
    --maroon-deep: #5a070b;
    --maroon-band: #6b0a10;
    --gold: #c9962e;
    --gold-light: #e8c063;
    --gold-dark: #9a6a18;
    --paper: #f4f4f4;
    --stage: #d9d9d9;
  }
  * { box-sizing: border-box; margin: 0; padding: 0; }
  html, body { width: 1200px; height: 1021px; overflow: hidden; }
  body { background: var(--stage); position: relative; font-family: "Tinos", serif; }

  .card {
    position: absolute; left: 220px; width: 760px; height: 434px;
    overflow: hidden; box-shadow: 0 6px 18px rgba(0,0,0,.25);
  }
  .card--front { top: 54px; background: radial-gradient(ellipse at 50% 40%, #8e1118 0%, var(--maroon) 55%, var(--maroon-deep) 100%); }
  .card--back { top: 533px; background: var(--paper); }

  .temple-backdrop {
    position: absolute; left: 170px; top: 40px; width: 420px; height: 270px;
    background: radial-gradient(ellipse at 50% 60%, rgba(60,4,8,.45), rgba(60,4,8,0) 70%);
  }

  .elephant {
    position: absolute; border-radius: 10px;
    background: linear-gradient(160deg, var(--gold-light), var(--gold) 45%, var(--maroon) 100%);
  }
  .card--front .elephant--left { left: 40px; top: 70px; width: 170px; height: 190px; }
  .card--front .elephant--right { right: 40px; top: 150px; width: 170px; height: 190px; }
  .card--back .elephant--left { left: 40px; top: 36px; width: 150px; height: 172px; }
  .card--back .elephant--right { right: 40px; top: 116px; width: 140px; height: 162px; }

  .tagline {
    position: absolute; left: 0; right: 0; top: 110px; text-align: center;
    font-family: "Kurale", serif; font-size: 30px; color: var(--gold);
  }
  .brand-name {
    position: absolute; left: 0; right: 0; top: 152px; text-align: center;
    font-family: "Kurale", serif; font-size: 46px; color: var(--gold);
  }
  .card--back .tagline { top: 84px; font-size: 28px; }
  .card--back .brand-name { top: 122px; font-size: 42px; color: var(--maroon); }

  .band {
    position: absolute; left: 0; right: 0; bottom: 0; height: 112px;
    background: var(--maroon-band); border-top: 2px solid var(--gold);
  }
  .card--front .band { background: rgba(70,5,9,.55); }

  .band-medallion {
    position: absolute; left: 50%; top: -16px; width: 32px; height: 32px; margin-left: -16px;
    border-radius: 50%; background: var(--gold); border: 3px solid var(--maroon-band);
  }
  .band-web {
    position: absolute; left: 0; right: 0; top: 38px; text-align: center;
    font-size: 22px; letter-spacing: 3px; color: var(--gold);
  }

  .person { position: absolute; left: 0; right: 0; top: 196px; text-align: center; }
  .person-name { font-size: 28px; font-weight: 700; color: var(--gold-dark); }
  .person-role { font-size: 17px; color: var(--maroon); margin-top: 2px; }
  .address {
    position: absolute; left: 0; right: 0; top: 288px; text-align: center;
    font-size: 18px; color: var(--maroon);
  }

  .contacts { display: flex; justify-content: space-around; align-items: flex-start; height: 100%; }
  .contact { position: relative; text-align: center; color: var(--gold-light); font-size: 20px; padding-top: 40px; }
  .contact-icon {
    position: absolute; left: 50%; top: -18px; width: 36px; height: 36px; margin-left: -18px;
    border-radius: 50%; background: var(--gold); border: 3px solid var(--maroon-band);
    display: flex; align-items: center; justify-content: center;
  }
  .contact-icon svg { width: 18px; height: 18px; stroke: var(--maroon); fill: none; stroke-width: 2; }
</style>
</head>
<body>

<section class="card card--front" aria-label="Vorderseite">
  <div class="temple-backdrop" role="img" aria-label="Faint silhouette of an Indian palace in the background"></div>
  <div class="elephant elephant--left" role="img" aria-label="Decorated gold ceremonial elephant with parasol"></div>
  <div class="elephant elephant--right" role="img" aria-label="Decorated gold ceremonial elephant with parasol"></div>
  <p class="tagline">Ayurvedische Massagen</p>
  <p class="brand-name">Mirelo-Dant</p>
  <div class="band">
    <span class="band-medallion"></span>
    <p class="band-web">www.mirelo-dant.ch</p>
  </div>
</section>

<section class="card card--back" aria-label="Rückseite">
  <div class="elephant elephant--left" role="img" aria-label="Decorated gold ceremonial elephant with parasol"></div>
  <div class="elephant elephant--right" role="img" aria-label="Decorated gold ceremonial elephant with parasol"></div>
  <p class="tagline">Ayurvedische Massagen</p>
  <p class="brand-name">Mirelo-Dant</p>
  <div class="person">
    <p class="person-name">Lukas Brenner</p>
    <p class="person-role">President</p>
  </div>
  <p class="address">Nora Gasser, Mirelo-Dant, Lindenweg 14, 8853 Lachen (SZ)</p>
  <div class="band">
    <div class="contacts">
      <div class="contact">
        <span class="contact-icon"><svg viewBox="0 0 20 20"><rect x="2" y="5" width="16" height="11"/><path d="M2 5l8 6 8-6"/></svg></span>
        info@mirelo-dant.ch
      </div>
      <div class="contact">
        <span class="contact-icon"><svg viewBox="0 0 20 20"><rect x="6" y="2" width="8" height="16" rx="1.5"/><path d="M9 15h2"/></svg></span>
        +41 77 000 12 34
      </div>
      <div class="contact">
        <span class="contact-icon"><svg viewBox="0 0 20 20"><circle cx="10" cy="10" r="8"/><path d="M2 10h16M10 2c-3 3-3 13 0 16M10 2c3 3 3 13 0 16"/></svg></span>
        www.mirelo-dant.ch
      </div>
    </div>
  </div>
</section>

</body>
</html>
```